THE REVEL OF GLIMBROOK Prospectus/Deck

We need a prospectus/deck made for this Halloween event called THE REVEL OF GLIMBROOK. Attached is the writeup, our logo, some background photos you can use, and photos of the actual town site. For the town photos (4) could you try to make them look greyscale or smokey? I attached a sample Prospectus/Deck that was created for another event of ours to give you an idea of layout and pages.

```html
<!DOCTYPE html>
<html lang="en">
<head>
<meta charset="utf-8">
<title>The Revel of Glimbrook – Prospectus</title>
<link rel="stylesheet" href="https://fonts.googleapis.com/css2?family=Roboto:wght@400;500;700&family=Permanent+Marker&display=swap">
<style>
:root{
  --board:#f3f2f0;
  --ink:#141515;
  --ink-2:#1d1f1f;
  --text:#eceae4;
  --green:#7ba04a;
  --green-dark:#5d8534;
  --gold:#e6b543;
  --card:#7fa54c;
}
*{box-sizing:border-box;margin:0;padding:0}
html,body{width:1200px;height:1200px;overflow:hidden;background:var(--board)}
body{position:relative;font-family:"Roboto",Arial,sans-serif;color:var(--text)}
.page{position:absolute;width:543px;height:386px;overflow:hidden;background:linear-gradient(180deg,var(--ink) 0%,var(--ink-2) 100%);box-shadow:0 6px 14px rgba(0,0,0,.25)}
.page--welcome{left:41px;top:188px}
.page--about{left:619px;top:188px}
.page--vendors{left:41px;top:613px}
.page--sponsors{left:619px;top:613px}
.abs{position:absolute}
.photo{position:absolute}
.brand-name{font-family:"Roboto",Arial,sans-serif;font-weight:700;color:var(--green);letter-spacing:.5px;line-height:1.1}
.eyebrow{font-size:6.5px;color:var(--gold)}
.heading{font-family:"Permanent Marker",cursive;color:var(--green);font-size:16px;line-height:1.1;white-space:nowrap}
.subheading{font-family:"Permanent Marker",cursive;color:var(--gold);font-size:9px;white-space:nowrap}
.tagline{font-size:9px;color:var(--gold);font-weight:500}
.body{font-size:6.4px;line-height:9.4px;text-align:justify;color:var(--text)}
.label-green{font-size:6.8px;color:var(--green);font-weight:500}
.label-gold{font-size:6.8px;color:var(--gold);font-weight:500}
.page-no{position:absolute;top:12px;right:16px;width:9px;height:9px;border-radius:50%;background:var(--green);color:#1a1a1a;font-size:5px;font-weight:700;text-align:center;line-height:9px}
.details p{font-size:6.4px;line-height:12.5px}
.details span{color:var(--gold)}
.vendor-list{list-style:none}
.vendor-list li{font-size:6.4px;line-height:11.4px;display:flex;align-items:center;gap:8px}
.vendor-list svg{width:7px;height:7px;flex:none}
.tier{position:absolute;top:101px;width:163px;height:164px;background:var(--card);border-radius:4px;overflow:visible}
.tier__head{height:25px;background:var(--green-dark);border-radius:4px 4px 0 0;font-size:7.6px;color:#fff;padding:4px 0 0 30px;line-height:8.6px}
.tier__price{position:absolute;top:-5px;right:10px;width:60px;height:41px;background:var(--gold);color:#1b1b1b;font-weight:700;font-size:9.6px;line-height:11.5px;text-align:center;padding-top:5px;clip-path:polygon(0 0,100% 0,100% 100%,50% 86%,0 100%)}
.tier ul{list-style:none;padding:14px 7px 0 10px}
.tier li{font-size:6.2px;line-height:8.6px;color:#fff;padding:0 0 3px 8px;margin-bottom:3px;border-bottom:1px solid rgba(255,255,255,.25);position:relative;text-align:justify}
.tier li:last-child{border-bottom:none}
.tier li::before{content:"";position:absolute;left:0;top:3px;width:3px;height:3px;border-radius:50%;background:#fff}
.link{color:var(--gold)}
</style>
</head>
<body>

<!-- Page 1: Welcome -->
<section class="page page--welcome">
  <div class="photo" role="img" aria-label="Photo of a robed figure in a bone mask with branch antlers standing in an autumn forest" style="left:268px;top:0;width:275px;height:386px;background:radial-gradient(ellipse at 55% 45%,#5a3a25 0%,#3a2618 45%,#1c140e 100%)"></div>
  <div class="abs" style="left:0;top:0;width:272px;height:386px;background:linear-gradient(90deg,var(--ink) 90%,rgba(20,21,21,0))"></div>
  <div class="abs brand-name" style="left:18px;top:18px;font-size:5.5px;color:var(--gold);letter-spacing:2px">THE REVEL OF</div>
  <div class="abs brand-name" style="left:18px;top:27px;font-size:19px">GLIMBROOK</div>
  <div class="abs eyebrow" style="left:17px;top:94px">Welcome to</div>
  <h1 class="abs heading" style="left:17px;top:103px">THE REVEL OF GLIMBROOK</h1>
  <p class="abs tagline" style="left:17px;top:124px">Where Terror Meets Hollywood Magic!</p>
  <p class="abs body" style="left:17px;top:150px;width:212px">Step into our nightmare-inducing event set within a sprawling film studio lot at 1450 Concession Road 9, Ashgrove, Ontario L0B 2K4 which has been transformed into a chillingly realistic little town. As you enter, you will find yourself immersed in the eerie atmosphere of a bygone era, where each corner holds lurking horrors. Our haunted experience offers a unique opportunity for vendors to become part of the terror by occupying the shops that line the Main Street of this sinister town. From creepy curiosities to spine-chilling treats, your store front will become a focal point of fear, allowing visitors to not only scream but also shop amidst the horrors. Prepare for a spine-tingling journey like no other as you explore our haunted event in this hauntingly realistic town.</p>
  <p class="abs body" style="left:17px;top:283px;width:212px">The Revel of Glimbrook is an an exhilarating and spine-chilling haunted town experience that promises to deliver unforgettable thrills and scares. As we gear up for another terrifying season, we invite you to join us as a valued vendor or sponsor. This prospectus outlines the various opportunities available for your brand to be part of this highly anticipated event</p>
</section>

<!-- Page 2: About -->
<section class="page page--about">
  <div class="photo" role="img" aria-label="Photo of an actor in bloodied overalls leaning on a weathered wooden shop counter with a mounted animal head behind" style="left:0;top:0;width:294px;height:386px;background:linear-gradient(160deg,#cfcac0 0%,#a8a294 35%,#5e5548 70%,#3a3c4a 100%)"></div>
  <div class="abs" style="left:286px;top:0;width:12px;height:386px;background:linear-gradient(90deg,rgba(20,21,21,0),var(--ink))"></div>
  <div class="page-no">2</div>
  <div class="abs eyebrow" style="left:314px;top:98px">About</div>
  <h2 class="abs heading" style="left:314px;top:108px">THE REVEL OF GLIMBROOK</h2>
  <p class="abs body" style="left:314px;top:145px;width:212px">The Revel of Glimbrook is a premier haunted town attraction known for its immersive and interactive experience that pushes the boundaries of fear. Our haunted town offers a meticulously designed setting with elaborate sets, talented actors, and cutting-edge special effects to create an atmosphere of horror and suspense. We attract a diverse audience of thrill-seekers, horror enthusiasts, families, and groups of friends, ensuring a wide reach for your brand.</p>
  <h3 class="abs subheading" style="left:314px;top:242px">EVENT DETAILS:</h3>
  <div class="abs details" style="left:314px;top:258px">
    <p><span>Date:</span> October 6 – 31, 2023 (17 days)</p>
    <p><span>Location:</span> 1450 Concession Road 9, Ashgrove, Ontario L0B 2K4</p>
    <p><span>Website:</span> www.revelofglimbrook.ca</p>
  </div>
</section>

<!-- Page 3: Vendors -->
<section class="page page--vendors">
  <div class="photo" role="img" aria-label="Greyscale aerial photo of the empty main street of the town set lined with brick storefronts" style="left:0;top:0;width:543px;height:170px;background:linear-gradient(180deg,#d9d9d9 0%,#b0b0b0 30%,#6f6f6f 60%,#8d8d8d 100%)"></div>
  <svg class="abs" style="left:0;top:150px" width="543" height="30" viewBox="0 0 543 30" aria-hidden="true">
    <path d="M0 14 L60 11 L140 15 L230 10 L320 14 L410 9 L480 13 L543 11 L543 30 L0 30Z" fill="#161717"/>
  </svg>
  <div class="page-no">3</div>
  <h2 class="abs subheading" style="left:17px;top:184px;font-size:9.5px">VENDOR OPPORTUNITIES:</h2>
  <div class="abs label-green" style="left:17px;top:202px">ON-SITE VENDORS:</div>
  <p class="abs body" style="left:17px;top:215px;width:212px">Starting at $2500 + HST (per vendor; no sharing) depending on location and type of products/services sold and offered</p>
  <p class="abs body" style="left:17px;top:241px;width:212px">Set up your booth within the haunted town premises and showcase your products or services to a captive audience in one of the existing buildings. Your brand will be exposed to thousands of visitors throughout the event. Examples of suitable vendors include:</p>
  <ul class="abs vendor-list" style="left:17px;top:280px">
    <li><svg viewBox="0 0 8 8"><rect x="1" y="1" width="6" height="6" fill="none" stroke="#bbb" stroke-width=".8"/></svg>Halloween costume shops</li>
    <li><svg viewBox="0 0 8 8"><rect x="1" y="1" width="6" height="6" fill="none" stroke="#bbb" stroke-width=".8"/></svg>Horror-themed merchandise</li>
    <li><svg viewBox="0 0 8 8"><rect x="1" y="1" width="6" height="6" fill="none" stroke="#bbb" stroke-width=".8"/></svg>Local/Artisan food vendors (pre-packaged items)</li>
    <li><svg viewBox="0 0 8 8"><rect x="1" y="1" width="6" height="6" fill="none" stroke="#bbb" stroke-width=".8"/></svg>Face painting and special effects makeup artists</li>
    <li><svg viewBox="0 0 8 8"><circle cx="3.5" cy="3.5" r="2.3" fill="none" stroke="#bbb" stroke-width=".8"/><path d="M5 5 L7.4 7.4" stroke="#bbb" stroke-width=".8"/></svg>Paranormal investigators or ghost tour guides</li>
    <li><svg viewBox="0 0 8 8"><rect x="1" y="1" width="6" height="6" fill="none" stroke="#bbb" stroke-width=".8"/></svg>Novelty and souvenir vendors</li>
    <li><svg viewBox="0 0 8 8"><circle cx="4" cy="4" r="3" fill="none" stroke="#bbb" stroke-width=".8"/></svg>Psychic</li>
    <li><svg viewBox="0 0 8 8"><path d="M4 1 L7 7 L1 7Z" fill="none" stroke="#bbb" stroke-width=".8"/></svg>Metaphysical items and crystals</li>
  </ul>
  <div class="abs label-gold" style="left:315px;top:216px">FOOD TRUCKS $5000 + HST max of 3-4 total</div>
  <div class="abs label-green" style="left:315px;top:237px">Promotional Giveaways:</div>
  <p class="abs body" style="left:315px;top:250px;width:212px">Partner with us to provide branded merchandise or samples to be distributed to our visitors. This opportunity allows you to directly engage with attendees and create lasting impressions of your brand.</p>
  <div class="abs label-green" style="left:315px;top:292px">Exclusive Sponsorship:</div>
  <p class="abs body" style="left:315px;top:305px;width:212px">Become an exclusive sponsor of The Revel of Glimbrook. This comprehensive package offers maximum exposure and recognition for your brand. Benefits may include prominent logo placement, branding on event merchandise, on-site signage, social media promotions, and more. This option is ideal for businesses looking to establish a strong association with the haunted town and its audience.</p>
</section>

<!-- Page 4: Sponsorship -->
<section class="page page--sponsors">
  <div class="photo" role="img" aria-label="Dark stormy sky over a tall cornfield at dusk" style="left:0;top:0;width:543px;height:386px;background:linear-gradient(180deg,#2a302a 0%,#3a4534 35%,#2e3a26 60%,#151b12 100%)"></div>
  <div class="page-no">4</div>
  <h2 class="abs subheading" style="left:17px;top:32px">SPONSORSHIP TIERS:</h2>
  <p class="abs body" style="left:17px;top:51px;width:212px">We offer different sponsorship tiers to suit your marketing goals and budget. Please note that availability is limited for each tier, and commitments will be honored on a first-come, first-served basis. The sponsorship tiers include:</p>

  <div class="tier" style="left:17px">
    <div class="tier__head">1. Platinum<br>Sponsorship:</div>
    <div class="tier__price">$15,000 +<br>HST</div>
    <ul>
      <li>Prominent logo placement on all marketing materials, including website, posters, flyers, and social media promotions</li>
      <li>Exclusive branding on event merchandise</li>
      <li>On-site signage and banners featuring your brand</li>
      <li>Dedicated social media posts highlighting your sponsorship</li>
      <li>Recognition during event announcements and media interviews</li>
      <li>Complimentary tickets for your staff or clients</li>
    </ul>
  </div>
  <div class="tier" style="left:190px">
    <div class="tier__head">2. Gold<br>Sponsorship:</div>
    <div class="tier__price">$10,000 +<br>HST</div>
    <ul>
      <li>Logo placement on select marketing materials, including website, posters, and social media promotions</li>
      <li>On-site signage featuring your brand</li>
      <li>Social media mentions acknowledging your sponsorship</li>
      <li>Complimentary tickets for your staff or clients</li>
    </ul>
  </div>
  <div class="tier" style="left:363px">
    <div class="tier__head">3. Silver<br>Sponsorship:</div>
    <div class="tier__price">$5,000 +<br>HST</div>
    <ul>
      <li>Logo placement on event website and select marketing materials</li>
      <li>Exclusive branding on event merchandise</li>
      <li>On-site signage featuring your brand</li>
      <li>Complimentary tickets for your staff or clients</li>
    </ul>
  </div>

  <div class="abs body" style="left:17px;top:292px;width:212px">
    <p>We are open to customizing sponsorship packages to meet your specific needs and objectives.</p>
    <p style="margin-top:6px">If you are interested in becoming a vendor or sponsor for The Revel of Glimbrook, please contact us at the following: <span class="link">mara@nightfallevents.ca</span></p>
    <p style="margin-top:6px">We would be delighted to discuss the available opportunities in more detail and tailor a package that aligns with your brand's goals.</p>
  </div>
  <div class="abs" style="left:274px;top:294px;width:1px;height:72px;background:rgba(255,255,255,.35)"></div>
  <p class="abs body" style="left:312px;top:292px;width:215px;text-align:right">Do not miss the chance to be part of a frightfully fantastic experience that will haunt your customers' memories for years to come. Join The Revel of Glimbrook as a vendor or sponsor and make this haunted town season one to remember!</p>
  <div class="abs brand-name" style="right:16px;top:342px;font-size:4.6px;color:var(--gold);letter-spacing:1.6px;text-align:right">THE REVEL OF</div>
  <div class="abs brand-name" style="right:16px;top:349px;font-size:15px">GLIMBROOK</div>
</section>

</body>
</html>
```